Self Storage Company Needs Postcard Design & Flyer Needed

The name of our company is Tidy Locker Yard. We are going to be opening two brand new locations. I need a postcard designed that we will mail to several thousand addresses near our new locations. The postcard needs to announce the opening of our new locations and our special promotion.
I need to have a postcard design that is catchy and worded in a way that will get people to stop by the stores and when they do they will select a key and if that key opens the lock then they will win 3 months of free storage.
1. NOW OPEN! UNLOCK FREE RENT TODAY.
2. Stop by one of our brand new locations and test your luck. Draw a key and if it opens the lock you win three months of free storage.
3. Hurry in, limited time only.
4. These locations need to be listed on postcard:
Tidy Locker Yard
24815 Marlow Court
Noblesville, IN 46062
317.555.4820
Tidy Locker Yard
16200 Quenby Glen Road
Fishers, IN 46038
317-555-7136
5. website address: www.tidylockeryard.example
6. logo attached.
7. feel free to use any pixvault photos
8. I've attached a flyer that has amenities listed. Feel free to use as many as them as you would like.
I also need to have a 8.5" X 11" flyer designed to match the postcards that we will display in the offices.
Look and feel
Each slider illustrates characteristics of the customer's brand and the style your logo design should communicate.

```html
<!DOCTYPE html>
<html lang="en">
<head>
<meta charset="utf-8">
<title>Tidy Locker Yard – Grand Opening Postcard</title>
<link rel="stylesheet" href="https://fonts.googleapis.com/css2?family=Barlow:wght@600;700;800&family=Ubuntu:wght@500&display=swap">
<style>
  :root {
    --red: #d4161f;
    --red-dark: #a8141c;
    --yellow: #f5ec23;
    --green: #1e7a3a;
    --green-dark: #1c5a2c;
    --ink: #2b2b2d;
    --paper: #ffffff;
    --backdrop: #d9dadc;
    --photo-light: #eef1f5;
    --photo-mid: #cfd8e3;
    --photo-warm: #e9dcc6;
  }
  * { box-sizing: border-box; margin: 0; padding: 0; }
  html, body { width: 1020px; height: 1200px; overflow: hidden; background: var(--backdrop); }
  body { position: relative; font-family: "Barlow", sans-serif; }

  .card {
    position: absolute; left: 115px; width: 790px; height: 510px;
    background: var(--paper); overflow: hidden;
    box-shadow: 0 2px 6px rgba(0,0,0,.18);
  }
  .card--front { top: 80px; }
  .card--back { top: 610px; }

  /* FRONT */
  .headline {
    position: absolute; left: 48px; top: 14px;
    font-weight: 800; font-size: 92px; line-height: 1; letter-spacing: -1px;
    background: linear-gradient(180deg, var(--red) 0%, var(--red-dark) 100%);
    -webkit-background-clip: text; background-clip: text; color: transparent;
  }
  .subhead {
    position: absolute; left: 518px; top: 26px;
    font-weight: 800; font-size: 36px; line-height: 0.98; color: var(--ink); letter-spacing: -0.3px;
  }
  .promo-band {
    position: absolute; left: 0; top: 113px; width: 100%; height: 49px;
    background: linear-gradient(90deg, var(--red-dark), var(--red));
    color: var(--yellow); font-weight: 700; font-size: 13.5px; line-height: 18px;
    text-align: center; text-transform: uppercase; padding-top: 6px; letter-spacing: -0.1px;
  }
  .photo-front {
    position: absolute; left: 0; top: 162px; width: 100%; height: 296px;
    background: linear-gradient(100deg, var(--photo-warm) 0%, var(--photo-light) 35%, var(--photo-mid) 65%, var(--photo-light) 100%);
  }
  .location {
    position: absolute; top: 187px; width: 287px; height: 174px;
    border: 2px solid var(--green); background: rgba(255,255,255,.82);
    text-align: center; color: var(--ink);
  }
  .location--noblesville { left: 69px; }
  .location--fishers { left: 418px; }
  .location__tab { position: absolute; left: 26px; top: 20px; width: 231px; height: 32px; }
  .location__tab span {
    position: absolute; inset: 0; display: flex; align-items: center; justify-content: center;
    color: #fff; font-family: "Ubuntu", sans-serif; font-weight: 500; font-size: 19px;
  }
  .location__address { margin-top: 62px; font-weight: 600; font-size: 23px; line-height: 25px; }
  .location__phone { margin-top: 4px; font-weight: 800; font-size: 42px; color: var(--green-dark); letter-spacing: 0.5px; }

  .brand-name {
    position: absolute; color: var(--red); font-weight: 800; text-align: center; line-height: 1.1;
  }
  .card--front .brand-name { left: 39px; top: 388px; width: 110px; font-size: 28px; }

  .offer-shapes { position: absolute; left: 0; top: 0; }
  .offer-hurry {
    position: absolute; left: 380px; top: 402px; width: 410px; height: 49px;
    display: flex; align-items: center; justify-content: center;
    color: var(--red); font-weight: 800; font-size: 26px; text-transform: uppercase;
  }
  .offer-web {
    position: absolute; left: 340px; top: 453px; width: 450px; height: 57px;
    display: flex; align-items: center; justify-content: center;
    color: var(--yellow); font-weight: 800; font-size: 25px; text-transform: uppercase; letter-spacing: 0.3px;
  }

  /* BACK */
  .photo-back {
    position: absolute; left: 330px; top: 0; width: 460px; height: 100%;
    background: linear-gradient(90deg, var(--photo-mid) 0%, var(--photo-warm) 45%, rgba(255,255,255,.95) 80%, #fff 100%);
  }
  .panel-shapes { position: absolute; left: 0; top: 0; }
  .amenities {
    position: absolute; left: 44px; top: 36px; list-style: none;
    font-family: "Ubuntu", sans-serif; font-weight: 500; font-size: 16px; line-height: 20.8px; color: var(--green-dark);
  }
  .amenities li { position: relative; padding-left: 18px; }
  .amenities li::before {
    content: ""; position: absolute; left: 0; top: 8px; width: 6px; height: 6px; border-radius: 50%; background: var(--red);
  }
  .card--back .brand-name { left: 354px; top: 342px; width: 112px; font-size: 30px; }
  .stamp { position: absolute; left: 665px; top: 33px; width: 93px; height: 93px; border: 1.5px solid #222; background: #fff; }
  .address-line { position: absolute; left: 475px; width: 283px; height: 0; border-top: 1.5px solid #222; }
</style>
</head>
<body>

<section class="card card--front">
  <div class="headline">NOW OPEN!</div>
  <div class="subhead">UNLOCK FREE<br>RENT TODAY.</div>
  <div class="promo-band">Stop by one of our brand new locations and test your luck. Draw a key and if it<br>opens the lock you win three months of free storage.</div>
  <div class="photo-front" role="img" aria-label="Photo of a bright storage warehouse with shelving and cardboard boxes"></div>

  <div class="location location--noblesville">
    <svg class="location__tab" viewBox="0 0 231 32" preserveAspectRatio="none"><polygon points="14,0 217,0 231,32 0,32" fill="var(--green)"/></svg>
    <div class="location__tab"><span>Tidy Locker Yard</span></div>
    <p class="location__address">24815 Marlow Court<br>Noblesville, IN 46062</p>
    <p class="location__phone">317.555.4820</p>
  </div>
  <div class="location location--fishers">
    <svg class="location__tab" viewBox="0 0 231 32" preserveAspectRatio="none"><polygon points="14,0 217,0 231,32 0,32" fill="var(--green)"/></svg>
    <div class="location__tab"><span>Tidy Locker Yard</span></div>
    <p class="location__address">16200 Quenby Glen Road<br>Fishers, IN 46038</p>
    <p class="location__phone">317-555-7136</p>
  </div>

  <svg class="offer-shapes" width="790" height="510" viewBox="0 0 790 510">
    <polygon points="364,402 790,402 790,451 352,451" fill="var(--yellow)"/>
    <polygon points="352,451 790,451 790,453 351,453" fill="var(--green)"/>
    <defs>
      <linearGradient id="webBand" x1="0" x2="1" y1="0" y2="0">
        <stop offset="0" stop-color="var(--red-dark)"/><stop offset="1" stop-color="var(--red)"/>
      </linearGradient>
    </defs>
    <polygon points="351,453 790,453 790,510 320,510" fill="url(#webBand)"/>
  </svg>
  <div class="offer-hurry">Hurry in, limited time only</div>
  <div class="offer-web">www.tidylockeryard.example</div>

  <div class="brand-name">Tidy<br>Locker<br>Yard</div>
</section>

<section class="card card--back">
  <div class="photo-back" role="img" aria-label="Faded photo of warehouse aisle with tall shelves and stacked boxes"></div>
  <svg class="panel-shapes" width="790" height="510" viewBox="0 0 790 510">
    <polygon points="0,0 365,0 333,510 0,510" fill="var(--yellow)"/>
    <polygon points="365,0 371,0 339,510 333,510" fill="var(--red)"/>
    <polygon points="371,0 376,0 344,510 339,510" fill="var(--green)"/>
  </svg>
  <ul class="amenities">
    <li>Month-to-Month Leases</li>
    <li>Online Payments</li>
    <li>Gated Property Access</li>
    <li>24-Hour Video Monitoring</li>
    <li>Climate Control Available</li>
    <li>24-Hour Coded Access Available</li>
    <li>Convenient Loading Areas</li>
    <li>Discounted Pre-Pay Programs</li>
    <li>Tenant Referral Rewards</li>
    <li>Available Carts and Dollies</li>
    <li>Small, Medium &amp; Large Boxes</li>
    <li>Specialty Boxes</li>
    <li>2” Disc &amp; Cylinder Locks</li>
    <li>Furniture Covers</li>
    <li>Foam Packing Peanuts</li>
    <li>Bubble Wrap</li>
    <li>Stretch Cords</li>
    <li>Nylon Rope</li>
    <li>Moving Blankets</li>
    <li>Tape and Tape Gun</li>
    <li>And much, much more...</li>
  </ul>
  <div class="brand-name">Tidy<br>Locker<br>Yard</div>
  <div class="stamp"></div>
  <div class="address-line" style="top:353px"></div>
  <div class="address-line" style="top:396px"></div>
  <div class="address-line" style="top:439px"></div>
</section>

</body>
</html>
```